Tarvel Ridge LLC

Need Professional Business cards for New Investment Fund

Target Market(s)

High Quality investors

Industry/Entity Type

Financial

Contact Information for Business Card

Phone Number +1 555 284 6193
Name Pavel Orlinsky
Title Fund Manager
email po@FundTarvel.example
Website www.FundTarvel.example

Colors

Designer to choose colors to be used in the design.

Requirements
Must have
• Must have our Logo and all of the above. Must be made so lettering and loge can be raised

```html
<!DOCTYPE html>
<html lang="en">
<head>
<meta charset="utf-8">
<title>Tarvel Ridge LLC — Business Card</title>
<link rel="stylesheet" href="https://fonts.googleapis.com/css2?family=Mulish:wght@400;700&display=swap">
<style>
  :root {
    --stage: #2f3a32;
    --card: #ffffff;
    --card-shade: #ececec;
    --accent: #1fd60a;
    --ink: #2b2b2b;
    --mark: #3a4a3e;
  }
  * { margin: 0; padding: 0; box-sizing: border-box; }
  html, body {
    width: 1200px;
    height: 900px;
    overflow: hidden;
  }
  body {
    background: var(--stage);
    font-family: "Mulish", sans-serif;
    display: flex;
    align-items: center;
    justify-content: center;
  }
  .business-card {
    position: relative;
    width: 840px;
    height: 480px;
    background: radial-gradient(circle at 70% 60%, var(--card) 0%, var(--card) 45%, var(--card-shade) 100%);
    box-shadow: 0 10px 30px rgba(0,0,0,0.35);
  }
  .contact-block {
    position: absolute;
    left: 64px;
    top: 150px;
  }
  .person-name {
    color: var(--accent);
    font-weight: 700;
    font-size: 30px;
    letter-spacing: 0.2px;
  }
  .person-title {
    color: var(--ink);
    font-size: 21px;
    margin-top: 2px;
  }
  .contact-list {
    list-style: none;
    margin-top: 22px;
  }
  .contact-list li {
    display: flex;
    align-items: center;
    gap: 12px;
    color: var(--ink);
    font-size: 21px;
    line-height: 32px;
  }
  .contact-icon {
    width: 16px;
    height: 16px;
    flex: none;
  }
  .brand {
    position: absolute;
    right: 80px;
    top: 260px;
    display: flex;
    align-items: center;
    gap: 14px;
  }
  .brand-square {
    width: 30px;
    height: 30px;
    background: var(--accent);
  }
  .brand-name {
    color: var(--mark);
    font-weight: 700;
    font-size: 38px;
    letter-spacing: 2px;
    text-transform: uppercase;
  }
</style>
</head>
<body>
  <article class="business-card">
    <div class="contact-block">
      <h1 class="person-name">Pavel Orlinsky</h1>
      <p class="person-title">Fund Manager</p>
      <ul class="contact-list">
        <li>
          <svg class="contact-icon" viewBox="0 0 16 16" aria-hidden="true">
            <path d="M4 1.5 6.5 5 5 6.5c.8 1.8 2.7 3.7 4.5 4.5L11 9.5l3.5 2.5-1.5 2.5C7.5 14.5 1.5 8.5 1.5 3Z" fill="none" stroke="#1fd60a" stroke-width="1.6" stroke-linejoin="round"/>
          </svg>
          +1 555 284 6193
        </li>
        <li>
          <svg class="contact-icon" viewBox="0 0 16 16" aria-hidden="true">
            <rect x="1.5" y="3.5" width="13" height="9" fill="none" stroke="#1fd60a" stroke-width="1.6"/>
            <path d="M1.5 3.5 8 9l6.5-5.5" fill="none" stroke="#1fd60a" stroke-width="1.6"/>
          </svg>
          po@FundTarvel.example
        </li>
        <li>
          <svg class="contact-icon" viewBox="0 0 16 16" aria-hidden="true">
            <circle cx="8" cy="8" r="7" fill="#1fd60a"/>
            <path d="M1 8h14M8 1c-3 3.5-3 10.5 0 14M8 1c3 3.5 3 10.5 0 14" fill="none" stroke="#ffffff" stroke-width="1"/>
          </svg>
          www.FundTarvel.example
        </li>
      </ul>
    </div>
    <div class="brand">
      <span class="brand-square" aria-hidden="true"></span>
      <span class="brand-name">Tarvel Ridge</span>
    </div>
  </article>
</body>
</html>
```